Lantern Square, Steady Course. (Website Design)

We are launching a new bipartisan civic movement: Lantern Square. Steady Course.
The mission is this: Americans deserve a government that is legally required to serve them honestly.
We are looking for a world-class website designer capable of creating an emotionally powerful, modern, cinematic landing page experience that feels larger than politics.
This is not a campaign website for a political party or candidate. We are not looking for a red, white, and blue page with stripes, or American flags, or stock footage of smiling people in a voting booth. We are looking for an emotional and cinematic experience through and through.
The visual direction should feel:
Historic
Hopeful
American
Emotional
Cinematic
Trustworthy
Timeless
The goal is to make visitors feel that they are witnessing the beginning of something important and want to be part of it in the end.
Primary Objective:
Inspire visitors to participate in a one-minute survey and cast their vote.
The survey itself is extremely short and takes approximately one minute to complete.
Everything on the page should ultimately guide visitors toward this action while creating enough curiosity, trust, emotional engagement, and excitement that they feel compelled to take part in the movement.
Audience:
The audience is ordinary Americans across the political spectrum: Democrats, Republicans, Independents.
The design should feel unifying and welcoming.
It should avoid looking partisan, ideological, activist, or government-issued.
Creative Freedom:
We are intentionally giving designers substantial creative freedom.
We are not looking for someone to simply arrange content into predefined sections.
Instead, we are looking for a designer who can think strategically about user experience and persuasion.
The ideal design is as minimal as possible, but you may always:
Use as many sections as you believe are necessary.
Use as many images as you believe are necessary.
Include storytelling elements.
Include data visualizations.
Include timelines.
Include videos.
Include animations.
Include or exclude sections as you see fit.
Reorganize the flow entirely.
We uploaded some files containing text and section suggestions. You don’t have to use them.
We also uploaded some images to convey the general feel we’re looking for.
We are much more interested in the effectiveness of the overall experience than in any specific layout.
What success looks like:
Think outside the box.
Please do not create another generic political website. We have already explored those approaches.
We are looking for something different.
The winning design will be the one that most effectively guides visitors from curiosity to belief to participation.
When a visitor reaches the end of the experience, they should feel:
This is bigger than politics.
This is something I can support regardless of party.
This feels credible.
This feels hopeful.
I want to be part of this.
Use the survey results, the research findings, the principles, the storytelling, or any other elements you believe will help build trust and inspire participation.
Don't just impress us with flashy visuals. Impress us with a website experience that inspires people to become part of the movement and cast their vote.
The final call-to-action should feel like the natural conclusion of the journey, not a request for engagement.
Our goal is not simply to inform visitors. Our goal is to inspire them to cast their vote.
Prioritize emotional impact, storytelling, clarity, and persuasion over decorative design elements.
Final words:
Design a website experience that successfully inspires visitors to take the survey and cast their vote.
Think like a storyteller, not just a designer.
Thank you for your interest in the project.
Best of luck.

```html
<!DOCTYPE html>
<html lang="en">
<head>
<meta charset="utf-8">
<title>Lantern Square, Steady Course.</title>
<link rel="stylesheet" href="https://fonts.googleapis.com/css2?family=Inter:wght@400;500;600;700;800&family=Playfair+Display:ital,wght@0,500;0,600;1,500;1,600&display=swap">
<style>
:root{
  --navy:#1b2b66;
  --navy-deep:#142255;
  --red:#c8202b;
  --red-deep:#a8161f;
  --ink:#1d2433;
  --muted:#4a5164;
  --line:#e3e5ec;
  --soft:#f4f5f8;
  --white:#ffffff;
  --serif:"Playfair Display", Georgia, serif;
  --sans:"Inter", Arial, sans-serif;
}
*{margin:0;padding:0;box-sizing:border-box}
html,body{width:1200px;height:4938px;overflow:hidden}
body{font-family:var(--sans);color:var(--ink);background:var(--white);position:relative}
section,header,footer{position:relative;width:1200px;overflow:hidden}
em{font-style:italic}
.serif{font-family:var(--serif);font-weight:500}
.eyebrow{font-size:13px;font-weight:600;letter-spacing:.06em;color:var(--red);text-transform:uppercase}
.rule{width:52px;height:2px;background:var(--red)}

/* header */
.site-header{height:90px;border-top:4px solid var(--red);background:var(--white)}
.brand{position:absolute;left:144px;top:14px;display:flex;align-items:center;gap:10px}
.brand-dot{width:60px;height:60px;border-radius:50%;background:var(--navy)}
.brand-name{font-family:var(--sans);font-weight:700;font-size:12px;line-height:15px;color:var(--navy);text-transform:uppercase;width:150px}
.main-nav{position:absolute;left:487px;top:36px;display:flex;gap:27px;font-size:13px;font-weight:500;color:var(--ink)}
.vote-btn{position:absolute;left:932px;top:25px;width:126px;height:40px;border-radius:20px;background:var(--red);color:var(--white);font-size:13px;font-weight:600;display:flex;align-items:center;padding-left:20px}
.vote-btn .arr{position:absolute;right:6px;top:6px;width:28px;height:28px;border-radius:50%;background:var(--white)}

/* hero */
.hero{height:615px}
.hero-media{position:absolute;inset:0;background:
  radial-gradient(ellipse 420px 300px at 50% 38%,rgba(214,218,228,.55) 0%,rgba(214,218,228,0) 70%),
  linear-gradient(180deg,#22397a 0%,#3d5490 22%,#8d97ae 48%,#b7b9c0 62%,#6f7789 80%,#3a4663 100%)}
.hero-shade{position:absolute;inset:0;background:
  radial-gradient(ellipse 900px 520px at 50% 45%,rgba(20,34,85,0) 40%,rgba(12,22,60,.55) 100%),
  linear-gradient(180deg,rgba(20,34,85,.1) 0%,rgba(20,34,85,.35) 100%)}
.play{position:absolute;left:561px;top:300px;width:58px;height:58px;border:2px solid var(--white);border-radius:50%}
.hero-title{position:absolute;left:0;width:1200px;top:360px;text-align:center;font-family:var(--serif);font-weight:500;font-size:62px;line-height:1;color:var(--white);text-shadow:0 2px 14px rgba(10,20,50,.45)}
.hero-sub{position:absolute;left:0;width:1200px;top:440px;text-align:center;font-size:20px;line-height:34px;color:var(--white);text-shadow:0 1px 8px rgba(10,20,50,.5)}

.stats{position:absolute;left:140px;top:650px;width:918px;height:122px;background:var(--white);box-shadow:0 6px 24px rgba(20,34,85,.12);display:flex;z-index:2}
.stat{flex:1;display:flex;align-items:center;gap:14px;padding-left:32px;border-left:1px solid var(--line)}
.stat:first-child{border-left:0}
.stat-num{font-size:38px;font-weight:700;color:var(--navy);line-height:1}
.stat-cap{font-size:12px;color:var(--muted);text-transform:uppercase;margin-top:4px;line-height:15px}

/* mission */
.mission{height:574px}
.mission-bg{position:absolute;right:0;top:0;width:560px;height:574px;background:
  radial-gradient(ellipse 300px 420px at 70% 60%,rgba(205,211,224,.55) 0%,rgba(255,255,255,0) 75%)}
.mission-photo{position:absolute;left:140px;top:144px;width:454px;height:353px;border-left:7px solid var(--red);background:
  radial-gradient(circle 180px at 68% 30%,rgba(255,240,200,.95) 0%,rgba(255,214,150,.5) 40%,rgba(255,214,150,0) 75%),
  linear-gradient(160deg,#e9c08a 0%,#d59a5a 35%,#9b6a3e 60%,#3d4f86 85%,#2c3b6e 100%)}
.mission-copy{position:absolute;left:657px;top:202px;width:400px}
.mission-copy h2{font-size:42px;color:var(--navy);margin:8px 0 20px}
.mission-copy p{font-size:15.5px;line-height:21px;color:var(--ink);margin-bottom:19px}

/* about */
.about{height:491px;background:
  radial-gradient(ellipse 500px 300px at 15% 40%,rgba(60,80,150,.35) 0%,rgba(60,80,150,0) 70%),
  linear-gradient(180deg,#1f326f 0%,#2a3574 55%,#b1253a 100%)}
.about-copy{position:absolute;left:142px;top:86px;width:390px;color:var(--white)}
.about-copy .eyebrow{color:var(--white)}
.about-copy h2{font-size:42px;margin:10px 0 8px}
.about-copy .rule{background:var(--white);margin-bottom:22px}
.about-copy p{font-size:15px;line-height:21px;margin-bottom:20px}
.about-grid{position:absolute;left:583px;top:78px;width:473px;height:336px;display:grid;grid-template-columns:repeat(3,1fr);grid-template-rows:repeat(2,1fr);gap:6px}
.portrait{background:radial-gradient(ellipse 70% 60% at 50% 40%,#8a8580 0%,#3a3632 70%,#1c1a18 100%)}
.portrait.warm{background:radial-gradient(ellipse 70% 60% at 50% 40%,#d2ae7e 0%,#7a5634 65%,#3b2816 100%)}
.portrait.cool{background:radial-gradient(ellipse 70% 60% at 50% 40%,#c4c8cf 0%,#5d6472 65%,#262a33 100%)}

/* journey */
.journey{height:690px}
.center-head{position:absolute;left:0;width:1200px;text-align:center}
.center-head h2{font-size:44px;color:var(--navy);margin-top:10px}
.center-head .rule{margin:6px auto 0}
.timeline-line{position:absolute;left:71px;top:374px;width:1058px;height:2px;background:linear-gradient(90deg,var(--red) 0 50%,var(--navy) 50% 100%)}
.pin{position:absolute;width:14px;height:14px;border-radius:50%;border:3px solid var(--red);background:var(--white);top:368px}
.pin.blue{border-color:var(--navy)}
.stem{position:absolute;width:2px;background:var(--red)}
.stem.blue{background:var(--navy)}
.milestone{position:absolute;width:211px}
.tag{display:inline-block;font-size:10px;font-weight:600;color:var(--white);padding:3px 7px;text-transform:uppercase}
.tag.navy{background:var(--navy)}
.tag.red{background:var(--red)}
.m-card{background:var(--white);box-shadow:3px 3px 0 #d6d8df,0 2px 10px rgba(0,0,0,.08);padding:14px 14px 14px 20px;font-size:12.5px;line-height:21px;color:var(--ink);height:117px}
.journey-note{position:absolute;left:0;width:1200px;top:594px;text-align:center;font-size:17px;font-weight:500}

/* principles */
.principles{height:1029px;background:var(--soft)}
.principles-photo{position:absolute;left:140px;top:191px;width:498px;height:690px;background:
  radial-gradient(ellipse 260px 220px at 60% 35%,rgba(190,120,170,.35) 0%,rgba(190,120,170,0) 70%),
  linear-gradient(180deg,#2e3680 0%,#6a2f72 35%,#b3283f 65%,#e0303c 100%)}
.principle{position:absolute;left:600px;display:flex;align-items:center;gap:24px}
.p-icon{width:68px;height:68px;border-radius:50%;background:var(--white);box-shadow:0 2px 8px rgba(0,0,0,.12);display:flex;align-items:center;justify-content:center;flex:none}
.p-icon span{width:52px;height:52px;border-radius:50%;background:var(--red);display:flex;align-items:center;justify-content:center}
.p-text{font-size:12.5px;line-height:21px;color:var(--ink);width:400px}
.agree{position:absolute;left:0;width:1200px;top:927px;display:flex;justify-content:center;align-items:center;gap:10px;font-size:17px;font-weight:500}

/* survey */
.survey{height:1200px}
.survey-card{position:absolute;left:142px;top:192px;width:922px;height:483px;background:var(--white);box-shadow:0 4px 20px rgba(20,34,85,.12)}
.s-row{position:absolute;left:23px;width:876px;display:flex;justify-content:space-between;align-items:center;border-bottom:1px solid var(--line);height:60px}
.s-row .label{font-size:15px;font-weight:700;color:var(--navy)}
.s-row .val{font-size:32px;font-weight:800;color:var(--red)}
.stress{position:absolute;left:19px;top:335px;width:884px;height:121px;background:#e9ecf3;text-align:center;font-size:12.5px;color:var(--ink);line-height:28px;padding-top:20px}
.stress b{font-weight:600;color:#1e7a3c}
.tick{display:inline-block;width:12px;height:12px;background:#2ea44f;border-radius:2px;vertical-align:-1px;margin-right:3px}

.cta{position:absolute;left:142px;top:755px;width:922px;height:363px;background:
  radial-gradient(ellipse 380px 260px at 75% 50%,rgba(230,80,90,.35) 0%,rgba(230,80,90,0) 70%),
  linear-gradient(120deg,var(--red-deep) 0%,var(--red) 60%,#b81c28 100%)}
.cta h2{position:absolute;left:42px;top:48px;font-size:39px;line-height:48px;font-weight:600;color:var(--white);width:600px}
.cta h2 em{font-family:var(--serif);font-weight:500}
.cta p{position:absolute;left:42px;top:210px;width:540px;font-size:12px;line-height:20px;color:var(--white)}
.cta-btn{position:absolute;left:42px;top:273px;width:134px;height:42px;border-radius:21px;background:var(--white);color:var(--navy);font-size:13px;font-weight:600;display:flex;align-items:center;justify-content:center;gap:8px}
.cta-count{position:absolute;left:665px;top:79px;width:186px;height:207px;background:var(--white);text-align:center;padding-top:20px}
.cta-count .num{font-size:54px;font-weight:800;color:var(--navy);line-height:1;margin-top:8px}
.cta-count .cap{font-size:12px;line-height:16px;color:var(--navy);margin-top:6px}

/* footer */
.site-footer{height:249px;background:var(--navy-deep)}
.f-brand{position:absolute;left:0;width:1200px;top:50px;display:flex;justify-content:center;align-items:center;gap:10px}
.f-brand .brand-dot{background:var(--white);width:64px;height:64px}
.f-brand .brand-name{color:var(--white)}
.socials{position:absolute;left:0;width:1200px;top:127px;display:flex;justify-content:center;gap:12px}
.socials span{width:30px;height:30px;border-radius:50%;border:1.5px solid var(--white)}
.socials span:first-child{background:var(--red);border-color:var(--red)}
.f-line{position:absolute;left:118px;top:178px;width:964px;height:1px;background:rgba(255,255,255,.2)}
.copyright{position:absolute;left:0;width:1200px;top:210px;text-align:center;font-size:12px;color:var(--white)}
</style>
</head>
<body>

<header class="site-header">
  <div class="brand"><span class="brand-dot"></span><span class="brand-name">Lantern Square, Steady Course.</span></div>
  <nav class="main-nav"><span>MISSION</span><span>JOURNEY</span><span>PRINCIPLES</span><span>EVIDENCE</span><span>ACT NOW</span></nav>
  <div class="vote-btn">VOTE YES<span class="arr"><svg width="28" height="28" viewBox="0 0 28 28"><path d="M10 18 L18 10 M12 10 H18 V16" stroke="#c8202b" stroke-width="1.6" fill="none"/></svg></span></div>
</header>

<section class="hero">
  <div class="hero-media" role="img" aria-label="Photograph of a domed capitol building under a deep blue sky"></div>
  <div class="hero-shade"></div>
  <div class="play"><svg width="54" height="54" viewBox="0 0 54 54"><path d="M22 18 L36 27 L22 36 Z" fill="#fff"/></svg></div>
  <h1 class="hero-title">Lantern Square <em>Steady Course</em></h1>
  <p class="hero-sub">Americans deserve a government legally required to serve them honestly.<br>Not a promise — a binding obligation.</p>
</section>

<div class="stats">
  <div class="stat">
    <svg width="46" height="46" viewBox="0 0 46 46"><rect x="6" y="16" width="28" height="24" rx="3" fill="none" stroke="#c8202b" stroke-width="3"/><rect x="14" y="4" width="16" height="20" rx="2" fill="#c8202b"/><path d="M17 13 l3 3 6-6" stroke="#fff" stroke-width="2" fill="none"/></svg>
    <div><div class="stat-num">82.9%</div><div class="stat-cap">Said yes in a ballot vote.</div></div>
  </div>
  <div class="stat">
    <svg width="46" height="46" viewBox="0 0 46 46"><path d="M23 6 V40 M10 14 H36 M6 28 L10 14 L14 28 Z M32 28 L36 14 L40 28 Z M14 40 H32" stroke="#c8202b" stroke-width="3" fill="none"/></svg>
    <div><div class="stat-num">89.9%</div><div class="stat-cap">Said they agree with<br>the 7 principles.</div></div>
  </div>
  <div class="stat">
    <svg width="46" height="46" viewBox="0 0 46 46"><rect x="15" y="4" width="16" height="14" rx="2" fill="#c8202b"/><circle cx="10" cy="24" r="5" fill="#c8202b"/><circle cx="23" cy="24" r="5" fill="#c8202b"/><circle cx="36" cy="24" r="5" fill="#c8202b"/><path d="M4 42 v-8 a6 6 0 0 1 12 0 v8 M17 42 v-8 a6 6 0 0 1 12 0 v8 M30 42 v-8 a6 6 0 0 1 12 0 v8" fill="#c8202b"/></svg>
    <div><div class="stat-num">1,016</div><div class="stat-cap">People already voted for it.</div></div>
  </div>
</div>

<section class="mission">
  <div class="mission-bg" role="img" aria-label="Faint photograph of a capitol dome"></div>
  <div class="mission-photo" role="img" aria-label="Photograph of a flag and a bronze monument in warm golden sunlight"></div>
  <div class="mission-copy">
    <div class="eyebrow">Core Purpose</div>
    <h2 class="serif">Mission <em>Statement</em></h2>
    <p>Today, not a single law binds our government to act honestly, and in our best interest.</p>
    <p>If our government exists solely to serve us, Why isn't it legally required to?</p>
    <p>We founded this movement to change that.</p>
  </div>
</section>

<section class="about">
  <div class="about-copy">
    <div class="eyebrow">About Us</div>
    <h2 class="serif">Who <em>We Are</em></h2>
    <div class="rule"></div>
    <p>We are a bipartisan movement based in Washington, D.C.</p>
    <p>We believe Americans deserve a government legally required to act honestly, transparently, and in the public's best interest.</p>
    <p>At a time of growing division and distrust, we are working to unite Americans around a simple idea: government should faithfully serve the people, not special interests.</p>
  </div>
  <div class="about-grid">
    <div class="portrait" role="img" aria-label="Historic black and white portrait of a civic leader"></div>
    <div class="portrait warm" role="img" aria-label="Historic portrait of a civil rights leader"></div>
    <div class="portrait cool" role="img" aria-label="Historic black and white portrait of an activist"></div>
    <div class="portrait cool" role="img" aria-label="Historic portrait of a statesman speaking"></div>
    <div class="portrait warm" role="img" aria-label="Historic portrait of a reformer"></div>
    <div class="portrait" role="img" aria-label="Historic photograph of a leader addressing a crowd"></div>
  </div>
</section>

<section class="journey">
  <div class="center-head" style="top:76px">
    <div class="eyebrow">Our Journey</div>
    <h2 class="serif">Our Journey To A <em>National Movement</em></h2>
    <div class="rule"></div>
  </div>
  <div class="timeline-line"></div>

  <div class="pin" style="left:143px"></div>
  <div class="stem" style="left:149px;top:382px;height:40px"></div>
  <div class="pin blue" style="left:376px"></div>
  <div class="stem blue" style="left:382px;top:334px;height:34px"></div>
  <div class="pin" style="left:610px"></div>
  <div class="stem" style="left:616px;top:382px;height:40px"></div>
  <div class="pin blue" style="left:846px"></div>
  <div class="stem blue" style="left:852px;top:334px;height:34px"></div>

  <div class="milestone" style="left:376px;top:200px"><span class="tag navy">October 2025</span>
    <div class="m-card">We identified 10 principles that most of Americans agree our government must uphold.</div></div>
  <div class="milestone" style="left:843px;top:200px"><span class="tag navy">April 2026</span>
    <div class="m-card">We tested the framework in a pre-registered national study with Americans across the political spectrum.</div></div>
  <div class="milestone" style="left:142px;top:422px"><span class="tag red">August 2024</span>
    <div class="m-card">We started a nonprofit with this goal in mind: Americans deserve an honest government.</div></div>
  <div class="milestone" style="left:610px;top:422px"><span class="tag red">March 2026</span>
    <div class="m-card">We turned those principles into a rigorous framework and named it Lantern Square, Steady Course.</div></div>

  <p class="journey-note">And The Results Exceeded All Our Expectation.</p>
</section>

<section class="principles">
  <div class="center-head" style="top:78px">
    <div class="eyebrow">Our Journey</div>
    <h2 class="serif">The Seven <em>Principles</em></h2>
    <div class="rule"></div>
  </div>
  <div class="principles-photo" role="img" aria-label="Photograph of a protester before a capitol dome, toned navy to red"></div>

  <div class="principle" style="top:222px"><div class="p-icon"><span><svg width="26" height="26" viewBox="0 0 26 26"><circle cx="13" cy="6" r="4" fill="#fff"/><circle cx="6" cy="14" r="3.5" fill="#fff"/><circle cx="20" cy="14" r="3.5" fill="#fff"/><rect x="4" y="19" width="18" height="5" rx="2" fill="#fff"/></svg></span></div>
    <p class="p-text">Public officials should only serve the public good.<br>Not private interests.</p></div>
  <div class="principle" style="top:314px"><div class="p-icon"><span><svg width="26" height="26" viewBox="0 0 26 26"><path d="M7 24 V10 M11 24 V5 M15 24 V5 M19 24 V10 M5 24 H21" stroke="#fff" stroke-width="2.5" fill="none"/></svg></span></div>
    <p class="p-text">Major government decisions should be based on truth, and rigorous evidence. Not party loyalty, pressure, or donors.</p></div>
  <div class="principle" style="top:406px"><div class="p-icon"><span><svg width="26" height="26" viewBox="0 0 26 26"><path d="M13 3 V23 M4 8 H22 M8 23 H18" stroke="#fff" stroke-width="2.5" fill="none"/><path d="M2 16 L5 8 L8 16 Z M18 16 L21 8 L24 16 Z" fill="#fff"/></svg></span></div>
    <p class="p-text">When a public decision is made, people should be able to see the reasoning. Clearly. Honestly. On the record.</p></div>
  <div class="principle" style="top:498px"><div class="p-icon"><span><svg width="26" height="26" viewBox="0 0 26 26"><path d="M3 23 L11 13 L15 17 L23 5" stroke="#fff" stroke-width="2.5" fill="none"/><path d="M18 5 H23 V10" stroke="#fff" stroke-width="2.5" fill="none"/></svg></span></div>
    <p class="p-text">And if the government reasoning is flawed, citizens should have a way to challenge it, And get a real response.</p></div>
  <div class="principle" style="top:590px"><div class="p-icon"><span><svg width="26" height="26" viewBox="0 0 26 26"><path d="M4 10 H10 L19 4 V22 L10 16 H4 Z" fill="#fff"/></svg></span></div>
    <p class="p-text">Conflicts of interest in public office all should be disclosed, Before decisions are made.</p></div>
  <div class="principle" style="top:682px"><div class="p-icon"><span><svg width="26" height="26" viewBox="0 0 26 26"><path d="M13 2 V6 M7 12 a6 6 0 0 1 12 0 Z M5 13 H21 M7 14 V21 M11 14 V21 M15 14 V21 M19 14 V21 M3 23 H23" stroke="#fff" stroke-width="2.2" fill="#fff"/></svg></span></div>
    <p class="p-text">Lying or misleading the public in official decisions should carry consequences. Real ones.</p></div>
  <div class="principle" style="top:774px"><div class="p-icon"><span><svg width="26" height="26" viewBox="0 0 26 26"><circle cx="13" cy="13" r="10" stroke="#fff" stroke-width="2.5" fill="none"/><path d="M6 20 L20 6" stroke="#fff" stroke-width="2.5"/></svg></span></div>
    <p class="p-text">And most importantly, Money should never outweigh people's voice.</p></div>

  <div class="agree"><svg width="24" height="24" viewBox="0 0 24 24"><circle cx="12" cy="12" r="10" stroke="#1b2b66" stroke-width="2" fill="none"/><path d="M7 12 l3.5 3.5 L17 9" stroke="#1b2b66" stroke-width="2" fill="none"/></svg>89.9%* Said Agree.</div>
</section>

<section class="survey">
  <div class="center-head" style="top:76px">
    <div class="eyebrow">The Survey</div>
    <h2 class="serif">The <em>Survey</em></h2>
    <div class="rule"></div>
  </div>
  <div class="survey-card">
    <div class="s-row" style="top:12px"><span class="label">National Pre-Registered Study (N=2,500 Representative)</span><span class="val">89.9%</span></div>
    <div class="s-row" style="top:79px"><span class="label">Agree With The 7 Principles</span><span class="val">89.9%</span></div>
    <div class="s-row" style="top:144px"><span class="label">Support Legal Framework Built Around Them</span><span class="val">82.9%</span></div>
    <div class="s-row" style="top:209px"><span class="label">Neutral</span><span class="val">14.4%</span></div>
    <div class="s-row" style="top:272px;border-bottom:0"><span class="label">Actively Opposed</span><span class="val">2.7%</span></div>
    <div class="stress">
      STRESS TEST — Full Legal Framework, Enforcement Model, Actual Mechanism. Support HELD.<br>
      <b><span class="tick"></span>Democrats: 84.5%</b> | <b><span class="tick"></span>Republicans: 80.2%</b> | <b><span class="tick"></span>Independents: 79.9%</b><br>
      They All Said YES.
    </div>
  </div>

  <div class="cta">
    <h2>We Deserve A Government Legally Required <em>To Serve The People Honestly.</em></h2>
    <p>Across Political Lines, Generations, And Races, Americans Are Arriving At The Same Conclusion. And We Don't Have To Ask For It. We Just Have To Vote For It.</p>
    <div class="cta-btn">VOTE YES <svg width="20" height="12" viewBox="0 0 20 12"><path d="M1 6 H18 M13 1 L18 6 L13 11" stroke="#1b2b66" stroke-width="1.6" fill="none"/></svg></div>
    <div class="cta-count">
      <svg width="50" height="50" viewBox="0 0 50 50"><rect x="14" y="4" width="22" height="38" rx="4" fill="none" stroke="#c8202b" stroke-width="3"/><rect x="8" y="18" width="18" height="16" rx="2" fill="#c8202b"/><path d="M12 26 l3 3 6-6" stroke="#fff" stroke-width="2" fill="none"/></svg>
      <div class="num">1016</div>
      <div class="cap">People Already Voted<br>Yes For The Ballot</div>
    </div>
  </div>
</section>

<footer class="site-footer">
  <div class="f-brand"><span class="brand-dot"></span><span class="brand-name">Lantern Square, Steady Course.</span></div>
  <div class="socials"><span></span><span></span><span></span><span></span></div>
  <div class="f-line"></div>
  <p class="copyright">© 2026 LANTERN SQUARE, STEADY COURSE. All Rights Reserved.</p>
</footer>

</body>
</html>
```